Humorous Book by Comedian Needs E-book Cover

My book 'A Kettle on the Porch' is on Leafpad but I want a better cover designed. Cover needs my photo on it. My name is the most important text (because I have an existing audience.)

Text elements:
Author: Dorvel Pim
Title: A Kettle on the Porch
Subtitle: Tenth Anniversary Edition
Review Quote: 'All of his columns are amusing. The best are masterpieces.' Harbour Ledger

Above my name it should say: Collected Humour From NZ's Award-Winning Comedian

Here's the present version (which is why I want an improved version!)
http://www.brightmart-example.com/A-Kettle-Porch-Anniversary-Edition-ebook/dp/Q77TX2M904

Book covers I admire:

http://www.brightmart-example.co.uk/Why-The-Fern-Odile-Brask-ebook/dp/Q3318ZR7LN/ref=tmm_kin_title_0

http://www.brightmart-example.com/Gravelhat-Mira-Dunst-ebook/dp/Q691PLE583/ref=tmm_kin_title_0

http://www.brightmart-example.co.uk/Why-Keep-Lantern-Rex-Palfrey-ebook/dp/Q58JN3TQ7V

Leafpad covers need to work as thumbnails, as well as on small device screens.

This cover is for Brightmart Leafpad. Tech specs are on Leafpad Direct Publishing page. Dimensions: Requirements for the size of your cover art have an ideal height/width ratio of 1.6, this means: • A minimum of 625 pixels on the shortest side and 1000 pixels on the longest side • For best quality, your image would be 2820 pixels on the shortest side and 4500 pixels on the longest side

Dimensions Requirements for the size of your cover art have an ideal height/width ratio of 1.6, this means: • A minimum of 625 pixels on the shortest side and 1000 pixels on the longest side • For best quality, your image would be 2820 pixels on the shortest side and 4500 pixels on the longest side

Comedian

```html
<!DOCTYPE html>
<html lang="en">
<head>
<meta charset="utf-8">
<title>A Kettle on the Porch — Dorvel Pim</title>
<link rel="stylesheet" href="https://fonts.googleapis.com/css2?family=Courier+Prime:wght@700&family=Tinos:wght@400;700&display=swap">
<style>
  :root {
    --stage: #e4e7e7;
    --cover-light: #f4f4f4;
    --cover-mid: #d9d9d9;
    --ink: #111111;
    --photo-light: #f1ecdf;
    --photo-mid: #e6d9b8;
    --photo-dark: #b9a27c;
  }
  * { margin: 0; padding: 0; box-sizing: border-box; }
  html, body {
    width: 1200px; height: 908px; overflow: hidden;
    background: var(--stage);
  }
  .cover {
    position: absolute; left: 280px; top: 24px;
    width: 640px; height: 860px;
    background: linear-gradient(160deg, var(--cover-light) 0%, var(--cover-mid) 100%);
    color: var(--ink);
    overflow: hidden;
    box-shadow: 0 6px 24px rgba(0,0,0,.18);
  }
  .tagline {
    position: absolute; left: 18px; top: 30px;
    font: 700 15px/1 "Tinos", serif;
  }
  .author {
    position: absolute; right: 22px; top: 14px;
    font: 700 44px/1 "Tinos", serif;
  }
  .review {
    position: absolute; right: 22px; top: 66px;
    text-align: right;
    font: 400 17px/1.2 "Tinos", serif;
  }
  .author-photo {
    position: absolute; left: 350px; top: 140px;
    width: 290px; height: 640px;
    background: linear-gradient(180deg, var(--cover-light) 0%, var(--photo-light) 20%, var(--photo-mid) 60%, var(--photo-dark) 100%);
    -webkit-mask-image: linear-gradient(90deg, transparent 0, #000 14%, #000 100%);
    mask-image: linear-gradient(90deg, transparent 0, #000 14%, #000 100%);
  }
  .title {
    font-family: "Courier Prime", monospace; font-weight: 700;
  }
  .title .glyph { position: absolute; line-height: 1; }
  .title .big-a { font-size: 120px; }
  .title .kettle { font-size: 66px; }
  .title .small { font-size: 36px; }
  .title .porch {
    position: absolute; left: 282px; top: 556px;
    font-size: 64px; line-height: 1;
    writing-mode: vertical-rl;
  }
  .edition {
    position: absolute; right: 22px; bottom: 30px;
    font: 700 23px/1 "Tinos", serif;
  }
</style>
</head>
<body>
  <main class="cover">
    <p class="tagline">Collected Humour From NZ's Award-Winning Comedian</p>
    <p class="author">Dorvel Pim</p>
    <p class="review">“All of his columns are amusing.<br>The best are masterpieces.”<br>Harbour Ledger</p>
    <div class="author-photo" role="img" aria-label="Portrait of author Dorvel Pim in a cream jacket and bow tie, arms folded"></div>
    <h1 class="title" aria-label="A Kettle on the Porch">
      <span class="glyph big-a" style="left:26px;top:128px" aria-hidden="true">A</span>
      <span class="glyph kettle" style="left:36px;top:250px" aria-hidden="true">K</span>
      <span class="glyph kettle" style="left:62px;top:305px" aria-hidden="true">e</span>
      <span class="glyph kettle" style="left:88px;top:360px" aria-hidden="true">t</span>
      <span class="glyph kettle" style="left:114px;top:415px" aria-hidden="true">t</span>
      <span class="glyph kettle" style="left:140px;top:470px" aria-hidden="true">l</span>
      <span class="glyph kettle" style="left:166px;top:525px" aria-hidden="true">e</span>
      <span class="glyph small" style="left:222px;top:470px" aria-hidden="true">o</span>
      <span class="glyph small" style="left:222px;top:506px" aria-hidden="true">n</span>
      <span class="glyph small" style="left:252px;top:500px" aria-hidden="true">t</span>
      <span class="glyph small" style="left:252px;top:536px" aria-hidden="true">h</span>
      <span class="glyph small" style="left:252px;top:572px" aria-hidden="true">e</span>
      <span class="porch" aria-hidden="true">Porch</span>
    </h1>
    <p class="edition">Tenth Anniversary Edition</p>
  </main>
</body>
</html>
```